Small Accounting Practice needs something creative

We need a business card design for a new small accounting practice based in Perth, Australia. The name of the practice is 'Kowra Ledger Partners Pty Ltd'. We providing Tax, Bookkeeping and Accounting services. Our target are individuals and small businesses. We want the design to be simply and creative. Also, we can the design can help us to gain people's trust.

Target Market(s)

Individuals and small businesses.

Industry/Entity Type

Accounting

Colors

Designer to choose colors to be used in the design.

```html
<!DOCTYPE html>
<html lang="en">
<head>
<meta charset="utf-8">
<title>Kowra Ledger Partners – Business Card</title>
<link href="https://fonts.googleapis.com/css2?family=Exo+2:wght@400;600;700&family=Open+Sans:wght@400;700&display=swap" rel="stylesheet">
<style>
  :root {
    --teal: #2f8aa3;
    --ink: #111418;
    --stage: #161616;
    --card-dark: #1c1c1c;
    --panel-edge: #c4c4c4;
    --puzzle: #8a8889;
    --paper: #ffffff;
  }
  * { margin: 0; padding: 0; box-sizing: border-box; }
  html, body { width: 1200px; height: 1028px; overflow: hidden; }
  body { font-family: "Exo 2", sans-serif; background: var(--paper); position: relative; }

  .stage { position: absolute; left: 0; top: 0; width: 1200px; height: 785px; background: var(--stage); }
  .sheet { position: absolute; left: 0; top: 785px; width: 1200px; height: 243px; background: var(--paper); }

  .card { position: absolute; width: 520px; height: 300px; overflow: hidden; box-shadow: 0 14px 30px rgba(0,0,0,.55); }
  .card--front { background: var(--paper); }
  .card--back { background: var(--card-dark); }
  .card--mini { transform: scale(.5); transform-origin: top left; box-shadow: 0 8px 18px rgba(0,0,0,.35); }

  .puzzle-art { position: absolute; left: 26px; top: 22px; width: 130px; height: 110px;
    background: linear-gradient(135deg, var(--puzzle), #d8d8d8 70%, #fff); border-radius: 8px; }

  .wordmark { display: flex; align-items: center; gap: 10px; color: var(--teal); font-weight: 600; line-height: 1.05; }
  .wordmark__dot { flex: none; border-radius: 50%; background: var(--teal); }

  .card__brand { position: absolute; right: 28px; top: 30px; font-size: 21px; }
  .card__brand .wordmark__dot { width: 26px; height: 26px; }

  .contact { position: absolute; left: 250px; top: 112px; color: var(--ink); }
  .contact__name { font-size: 32px; font-weight: 600; letter-spacing: .5px; }
  .contact__name .first { color: var(--teal); font-weight: 600; }
  .contact__role { font-family: "Open Sans", sans-serif; font-size: 10.5px; font-weight: 700; margin: 2px 0 10px; }
  .contact__line { display: flex; align-items: center; gap: 8px; font-size: 15px; margin-bottom: 5px; }
  .contact__line--mail { font-size: 12.5px; }
  .contact__line svg { flex: none; fill: var(--teal); }

  .card__band { position: absolute; left: 0; bottom: 0; width: 100%; height: 52px;
    background: var(--card-dark); border-top: 5px solid var(--teal); }
  .card__agent { position: absolute; left: 16px; bottom: 12px; color: #e8e8e8;
    font-family: "Open Sans", sans-serif; font-size: 10px; }

  .back__panel { position: absolute; left: 34px; top: 26px; width: 452px; height: 248px;
    background: radial-gradient(ellipse at center, #fff 55%, #e9e9e9 100%);
    border: 9px solid var(--panel-edge); border-radius: 124px;
    display: flex; align-items: center; justify-content: center; }
  .back__panel .wordmark { font-size: 30px; }
  .back__panel .wordmark__dot { width: 40px; height: 40px; }

  .sheet__mark { position: absolute; left: 40px; top: 60px; font-size: 54px; }
  .sheet__mark .wordmark__dot { width: 96px; height: 96px; margin-right: 10px; }
</style>
</head>
<body>

<main class="stage">
  <article class="card card--front" style="left:95px; top:240px;">
    <div class="puzzle-art" role="img" aria-label="Grey jigsaw puzzle pieces fitting together"></div>
    <div class="card__brand wordmark"><span class="wordmark__dot"></span><span>Kowra Ledger<br>Partners Pty Ltd</span></div>
    <div class="contact">
      <p class="contact__name"><span class="first">Tom</span> Reyes</p>
      <p class="contact__role">Accountant &amp; Small Business Consultant</p>
      <p class="contact__line"><svg width="18" height="14" viewBox="0 0 18 14"><path d="M1 4c0-2 3-3 8-3s8 1 8 3v2h-4V4.5H5V6H1z"/><rect x="3" y="7" width="12" height="7" rx="1"/></svg>000-000-0000</p>
      <p class="contact__line contact__line--mail"><svg width="18" height="13" viewBox="0 0 18 13"><rect width="18" height="13" rx="1"/><path d="M1 1l8 6 8-6" stroke="#fff" stroke-width="1.4" fill="none"/></svg>tom@kowraledger.com.au</p>
    </div>
    <div class="card__band"><span class="card__agent">Registered ASIC Agent 40817</span></div>
  </article>

  <article class="card card--back" style="left:640px; top:240px;">
    <div class="back__panel">
      <div class="wordmark"><span class="wordmark__dot"></span><span>Kowra Ledger<br>Partners Pty Ltd</span></div>
    </div>
  </article>
</main>

<section class="sheet">
  <div class="sheet__mark wordmark"><span class="wordmark__dot"></span><span>Kowra Ledger<br>Partners Pty Ltd</span></div>

  <article class="card card--back card--mini" style="left:650px; top:40px;">
    <div class="back__panel">
      <div class="wordmark"><span class="wordmark__dot"></span><span>Kowra Ledger<br>Partners Pty Ltd</span></div>
    </div>
  </article>

  <article class="card card--front card--mini" style="left:925px; top:40px;">
    <div class="puzzle-art" role="img" aria-label="Grey jigsaw puzzle pieces fitting together"></div>
    <div class="card__brand wordmark"><span class="wordmark__dot"></span><span>Kowra Ledger<br>Partners Pty Ltd</span></div>
    <div class="contact">
      <p class="contact__name"><span class="first">Tom</span> Reyes</p>
      <p class="contact__role">Accountant &amp; Small Business Consultant</p>
      <p class="contact__line"><svg width="18" height="14" viewBox="0 0 18 14"><path d="M1 4c0-2 3-3 8-3s8 1 8 3v2h-4V4.5H5V6H1z"/><rect x="3" y="7" width="12" height="7" rx="1"/></svg>000-000-0000</p>
      <p class="contact__line contact__line--mail"><svg width="18" height="13" viewBox="0 0 18 13"><rect width="18" height="13" rx="1"/><path d="M1 1l8 6 8-6" stroke="#fff" stroke-width="1.4" fill="none"/></svg>tom@kowraledger.com.au</p>
    </div>
    <div class="card__band"><span class="card__agent">Registered ASIC Agent 40817</span></div>
  </article>
</section>

</body>
</html>
```